Private Equity Firm Investment Offering Pitchbook

Complete design of seven page investment teaser. Clients include high net worth, investment institutions (Perivale Lund, TQW, etc) and public/private investment partnerships.

This book will provide these clients a first look at our firm, provide for a brief overview of investment opportunities. This is the “first impression” document, sent both through email and printed / mailed.

Industry/Entity Type

Investment

Font styles to use
Serif

Colors
3176b5
85acd3

Requirements
Must have
• Please do not use the attached presentation for creative purposes. It is being provided purely to provide content of slides. Ty
Should not have
• White background only, thank you

```html
<!DOCTYPE html>
<html lang="en">
<head>
<meta charset="utf-8">
<title>Valerio Capital Partners – Pitchbook Pages</title>
<link rel="stylesheet" href="https://fonts.googleapis.com/css2?family=EB+Garamond:wght@400;500&family=Arimo:wght@400;700&display=swap">
<style>
:root{
  --blue:#3176b5;
  --blue-deep:#2a67a3;
  --blue-light:#85acd3;
  --blue-pale:#dbe7f3;
  --ink:#222;
  --ink-soft:#555;
  --canvas:#ebebeb;
  --panel-grey:#efefef;
  --white:#fff;
}
*{box-sizing:border-box;margin:0;padding:0}
html,body{width:1200px;height:1000px;overflow:hidden;background:var(--canvas)}
body{position:relative;font-family:"Arimo",Arial,sans-serif;color:var(--ink)}
.page{position:absolute;width:386px;height:293px;background:var(--white);overflow:hidden;box-shadow:0 0 2px rgba(0,0,0,.08)}
.page::before{content:"";position:absolute;left:0;top:0;width:100%;height:5px;background:#dcdcdc}
.page-title{position:absolute;left:14px;top:16px;font-family:"EB Garamond",Georgia,serif;font-size:19px;letter-spacing:.5px;color:var(--ink);text-transform:uppercase}
.brand{position:absolute;right:10px;top:12px;display:flex;align-items:center;gap:3px;font-family:"Arimo",Arial,sans-serif;font-weight:700;font-size:6px;letter-spacing:.6px;color:var(--blue)}
.brand .dot{width:8px;height:8px;border-radius:50%;background:var(--blue)}
.page-no{position:absolute;left:14px;bottom:6px;font-size:5px;color:var(--ink-soft)}
.page-rule{position:absolute;left:0;right:0;bottom:0;height:3px;background:var(--blue)}
.blue-panel{position:absolute;left:0;right:0;top:42px;height:228px;background:linear-gradient(160deg,var(--blue) 0%,var(--blue-deep) 100%);color:var(--white)}
.body-text{font-size:5.6px;line-height:1.32}
.body-text b{font-weight:700}
.photo{position:absolute}

/* cover page */
.cover .firm-name{position:absolute;left:14px;top:20px;font-family:"EB Garamond",Georgia,serif;font-size:17px;color:var(--ink);text-transform:uppercase}
.cover .photo{left:0;top:40px;width:386px;height:197px;background:linear-gradient(180deg,#5e6b78 0%,#3c4652 45%,#7f8a95 100%)}
.cover .accent{position:absolute;left:0;right:0;top:237px;height:4px;background:var(--blue)}
.cover .tagline{position:absolute;left:14px;top:250px;font-family:"EB Garamond",Georgia,serif;font-size:14px;color:var(--blue)}
.cover .presenter{position:absolute;left:14px;top:271px;font-size:6.5px}

/* title page */
.title-page .hero{position:absolute;left:0;top:0;width:386px;height:248px;background:linear-gradient(120deg,#2f6fad 0%,#3f7fbd 55%,#6b9cc9 100%)}
.title-page .hero .photo{right:0;top:0;width:180px;height:248px;background:linear-gradient(200deg,rgba(255,255,255,.35),rgba(133,172,211,.15) 60%,rgba(49,118,181,0))}
.title-page .hero h1{position:absolute;left:14px;top:50px;font-family:"EB Garamond",Georgia,serif;font-weight:400;font-size:17px;line-height:1.2;color:var(--white)}
.title-page .hero .line{position:absolute;left:14px;top:94px;width:185px;height:1px;background:rgba(255,255,255,.7)}
.title-page .hero .presenter{position:absolute;left:14px;top:101px;font-size:6.5px;color:var(--white)}
.title-page .firm-name{position:absolute;left:14px;top:262px;font-family:"EB Garamond",Georgia,serif;font-size:15px;text-transform:uppercase}
.title-page .brand{top:auto;bottom:12px}

/* investor opportunity */
.opportunity .intro{position:absolute;left:0;right:0;top:48px;height:60px;background:var(--blue);color:var(--white);padding:6px 14px 0;text-align:center}
.opportunity .terms-bar{position:absolute;left:0;right:0;top:108px;height:15px;background:var(--blue-light);color:var(--white);font-weight:700;font-size:7.5px;text-align:center;line-height:15px;letter-spacing:.3px}
.terms{position:absolute;left:14px;right:14px;top:131px;list-style:none}
.terms li{display:flex;align-items:center;gap:8px;min-height:20px;margin-bottom:3px;padding-bottom:3px;border-bottom:1px solid #e6e6e6}
.terms li:last-child{border-bottom:0}
.terms .num{flex:0 0 14px;height:14px;border-radius:50%;background:var(--blue-light);color:var(--white);font-size:6.5px;text-align:center;line-height:14px;font-weight:700}
.terms .body-text{color:var(--ink)}
.disclaimer{position:absolute;left:14px;right:14px;top:258px;font-size:3.6px;line-height:1.3;color:var(--ink-soft)}

/* two-column panels */
.cols{position:absolute;left:14px;right:14px;top:10px;bottom:10px;display:flex;gap:12px}
.cols .col{flex:1}
.cols .col + .col{border-left:1px solid rgba(255,255,255,.35);padding-left:12px}
.cols p{margin-bottom:4px}
.leader-role{font-family:"EB Garamond",Georgia,serif;font-weight:500;font-size:6px;text-transform:uppercase;letter-spacing:.3px;margin-top:3px}

/* performance */
.performance .lead-box{position:absolute;left:0;top:52px;width:150px;height:173px;background:var(--blue);color:var(--white);display:flex;align-items:center;justify-content:center;text-align:center;padding:0 14px;font-size:9.5px;line-height:1.3}
.points{position:absolute;left:132px;right:14px;top:52px;list-style:none}
.points li{display:flex;align-items:center;gap:9px;height:44px;border-bottom:1px solid #e3e3e3}
.points li:last-child{border-bottom:0}
.points .icon{flex:0 0 36px;height:36px;border-radius:50%;background:var(--blue);display:flex;align-items:center;justify-content:center;box-shadow:0 0 0 3px var(--blue-pale)}
.points .icon.light{background:var(--blue-light)}
.points .body-text{font-size:6px;color:var(--ink)}

/* management */
.management .pre{position:absolute;left:0;right:0;top:50px;height:75px;background:var(--blue);color:var(--white);padding:8px 14px}
.section-head{font-family:"EB Garamond",Georgia,serif;font-size:10px;text-transform:uppercase;margin-bottom:4px}
.management .post{position:absolute;left:0;top:125px;width:210px;height:150px;padding:8px 14px}
.management .post .section-head{color:var(--blue)}
.management .post ul{list-style:none;margin-top:6px}
.management .post li{font-size:5.4px;color:var(--ink-soft);padding:2px 0 3px 6px;border-bottom:1px solid #e4e4e4;position:relative}
.management .post li::before{content:"";position:absolute;left:0;top:4px;width:2px;height:2px;border-radius:50%;background:var(--blue-light)}
.management .aside{position:absolute;left:210px;right:0;top:125px;height:150px;background:var(--panel-grey);padding:10px 12px;color:var(--ink-soft)}
.management .aside p{margin-bottom:6px}

/* contact */
.contact .photo{left:0;top:58px;width:220px;height:194px;background:linear-gradient(135deg,#c9d3dc 0%,#8f9fae 50%,#56677a 100%)}
.contact .card{position:absolute;left:220px;right:0;top:58px;height:194px;background:var(--blue);color:var(--white);padding:0 14px}
.contact .avatar{position:absolute;left:16px;top:13px;width:40px;height:40px;border-radius:50%;background:linear-gradient(180deg,#c7b8a8,#8b7b6c);border:3px solid var(--white)}
.contact .name{position:absolute;left:14px;top:62px;font-family:"EB Garamond",Georgia,serif;font-weight:500;font-size:8px;text-transform:uppercase}
.contact .role{position:absolute;left:14px;top:73px;font-size:6px;font-weight:700}
.contact .address{position:absolute;left:14px;top:84px;font-size:5.3px;line-height:1.4}
.contact .reach{position:absolute;left:14px;top:132px;font-size:5.3px;line-height:1.5}
.contact .reach b{font-weight:700}
</style>
</head>
<body>

<!-- 1: Cover -->
<section class="page cover" style="left:14px;top:14px">
  <div class="firm-name">Valerio Capital Partners</div>
  <div class="brand"><span class="dot"></span>VALERIO</div>
  <div class="photo" role="img" aria-label="Photo of smiling business people seated at a conference table"></div>
  <div class="accent"></div>
  <div class="tagline">Private Capital Group “A Partner for the Long-Term”</div>
  <div class="presenter">Presenter Name</div>
</section>

<!-- 2: Title -->
<section class="page title-page" style="left:407px;top:14px">
  <div class="hero">
    <div class="photo" role="img" aria-label="Photo of a glass office tower seen from below, tinted blue"></div>
    <h1>Private Capital Group<br>“A Partner for the Long-Term”</h1>
    <div class="line"></div>
    <div class="presenter">Presenter Name</div>
  </div>
  <div class="firm-name">Valerio Capital Partners</div>
  <div class="brand"><span class="dot"></span>VALERIO</div>
</section>

<!-- 3: Investor opportunity -->
<section class="page opportunity" style="left:801px;top:14px">
  <h2 class="page-title">Investor Opportunity</h2>
  <div class="brand"><span class="dot"></span>VALERIO</div>
  <div class="intro body-text">It is our belief that industries in our area(s) of focus are well positioned within the economy, creating an opportune time to launch a boutique, SEC-registered <b>$100 million PE Fund</b>. The goal is to complete the asset raise by June 30, 2019 and immediately begin allocating. The amount and structure will allow us to access a wide array of investors, which in turn will yield the capital required to invest in a diverse portfolio of well-managed companies with <b>long-term growth prospects</b> within our area(s) of expertise.</div>
  <div class="terms-bar">INVESTMENT TERMS</div>
  <ol class="terms">
    <li><span class="num">1</span><span class="body-text">Invest alongside our clients. We are committed to <b>$5 million of the $100 million Fund.</b></span></li>
    <li><span class="num">2</span><span class="body-text"><b>5-7 year</b> investment term with a preferred rate of <b>8%</b>.</span></li>
    <li><span class="num">3</span><span class="body-text">Our fee schedule is aligned with the interests of investors. There is a <b>1% management fee and a 10% performance</b> incentive fee that will scale higher after specific investment performance hurdles have been achieved.</span></li>
    <li><span class="num">4</span><span class="body-text"><b>$250,000 minimum investment</b> is ideal for high net-worth individuals and smaller institutional entities.</span></li>
    <li><span class="num">5</span><span class="body-text">We are dedicated to forming <b>long-term investment partner relationships</b>. Those who can introduce us to <b>$10 million AUM</b> of investment capital (individual/pooled) will be provided co-investment opportunities on a deal by deal basis for <b>25% of the $10 million AUM commitment.</b></span></li>
  </ol>
  <p class="disclaimer">Disclaimer: This presentation is provided for informational purposes only and is intended to assist in considering the services offered by Valerio Capital Partners, LLC. Information contained herein has been furnished on a strictly confidential basis. It does not constitute an offer to sell or a solicitation of an offer to buy any security, nor is it advice or a recommendation to enter into any transaction. Any offer to sell or solicitation of an offer to buy will be made only by a Confidential Offering Memorandum. This information may not be reproduced or distributed in whole or in part without prior written consent. © Valerio Capital Partners, LLC 2019. All Rights Reserved.</p>
  <div class="page-no">3</div>
</section>

<!-- 4: Firm overview -->
<section class="page overview" style="left:14px;top:341px">
  <h2 class="page-title">Firm Overview</h2>
  <div class="brand"><span class="dot"></span>VALERIO</div>
  <div class="blue-panel">
    <div class="cols body-text">
      <div class="col">
        <p><b>Valerio Capital Partners</b> is a Chicago-based private equity firm that identifies companies with high potential for organic growth or industry consolidation in the industrial manufacturing sectors. Valerio invests in private, lower middle market companies with a minimum of $10 million in revenue, stable cash flow, and tenured management. Current investments include the following:</p>
        <p><b>Crestline Brass, LLC</b> (“Crestline Brass”) is the largest, US-based manufacturer of couplings, adapters, and related components used in the firefighting industry. Its products are used in critical, life-saving applications to help connect firefighting hoses to trucks and hydrants. In addition to firefighting, Crestline Brass’s products are also used for big water applications such as hydraulic fracturing wells, industrial fire suppression, and emergency water distribution.</p>
        <p><b>Halden Energy Services, LLC</b> (“HES”) provides components, maintenance, and repairs to gas turbines, centrifugal gas compressors, pumps, gearboxes, and generators to the energy industry. HES specializes in overhaul and parts manufacturing of leading turbine lines and is a certified distributor and repair center providing the highest quality repair and expertise concerning industrial valves.</p>
      </div>
      <div class="col">
        <p><b>Ashgrove Stainless Plate, LLC</b> (“ASP”) provides specialty and standard grades of stainless steel plate in some of the widest, thickest, and longest dimensions in North America. The mill portfolio includes key grades that offer significant weight savings as well as high mechanical strength for lighter and stronger stainless.</p>
        <p><b>Keystone Thermal</b> was founded in 1912 and has since serviced the automotive, air conditioning and refrigeration industries as a manufacturer of extruded aluminum shapes for heat transfer. Keystone is also a fabricator of all-aluminum and aluminum/copper heat transfer coils. A major supplier of heat transfer products to the Automotive, Aerospace, Off-road Truck, Heavy Equipment as well as residential and commercial refrigeration markets.</p>
      </div>
    </div>
  </div>
  <div class="page-no">4</div>
  <div class="page-rule"></div>
</section>

<!-- 5: Investment performance -->
<section class="page performance" style="left:407px;top:341px">
  <h2 class="page-title">Investment Performance</h2>
  <div class="brand"><span class="dot"></span>VALERIO</div>
  <div class="lead-box">A sample of return characteristics of previous investments include the following</div>
  <ul class="points">
    <li>
      <span class="icon"><svg width="16" height="16" viewBox="0 0 16 16" fill="none" stroke="#fff" stroke-width="1.2"><rect x="3" y="2" width="9" height="12" rx="1"/><path d="M5 5h5M5 7.5h5M5 10h3"/></svg></span>
      <span class="body-text">The results shown are for informational purposes only.</span>
    </li>
    <li>
      <span class="icon light"><svg width="16" height="16" viewBox="0 0 16 16" fill="none" stroke="#fff" stroke-width="1.2"><circle cx="8" cy="8" r="2"/><path d="M8 2v4M8 10v4M2 8h4M10 8h4"/></svg></span>
      <span class="body-text">The returns are net of fees and expenses and are self-reported.</span>
    </li>
    <li>
      <span class="icon"><svg width="16" height="16" viewBox="0 0 16 16" fill="none" stroke="#fff" stroke-width="1.3"><circle cx="7" cy="7" r="4"/><path d="M10 10l4 4"/></svg></span>
      <span class="body-text">These performance results are designed to highlight the Firm’s experience in previous SPV investments but are not designed to reflect potential returns of the proposed Fund.</span>
    </li>
    <li>
      <span class="icon light"><svg width="16" height="16" viewBox="0 0 16 16" fill="none" stroke="#fff" stroke-width="1.2"><circle cx="8" cy="9" r="5"/><path d="M8 9V6.5M6.5 2.5h3"/></svg></span>
      <span class="body-text">In fact, hypothetical performance results have many inherent limitations.</span>
    </li>
  </ul>
  <div class="page-no">5</div>
  <div class="page-rule"></div>
</section>

<!-- 6: Investment management -->
<section class="page management" style="left:801px;top:341px">
  <h2 class="page-title">Investment Management</h2>
  <div class="brand"><span class="dot"></span>VALERIO</div>
  <div class="pre">
    <h3 class="section-head">Pre-Investment</h3>
    <p class="body-text" style="font-size:6px">We conduct robust due diligence with the dual objective of ensuring that risk/reward attributes have been fully vetted and that a well-grounded executable investment thesis and business plan have been developed. We then capitalize each investment in a manner custom-designed to facilitate the execution of the investment thesis and business plan.</p>
  </div>
  <div class="post">
    <h3 class="section-head">Post-Investment</h3>
    <p class="body-text" style="font-size:6px">During our ownership period, we work collaboratively with each management team to ensure:</p>
    <ul>
      <li>Key investment assumptions are periodically confirmed or adjusted</li>
      <li>An environment of execution and accountability exists</li>
      <li>Internal and external reporting is timely, useful, and fully transparent</li>
      <li>Human and financial capital needs are identified and adequately met</li>
      <li>All stake holder interests are properly aligned</li>
    </ul>
  </div>
  <div class="aside body-text">
    <p>A consistent plan of communication is executed throughout the investment cycle. This ranges from monthly calls to having our operating executives on-site not only monitoring our investment but also providing day-to-day assistance in managing and growing these organizations.</p>
    <p>We will utilize all necessary resources to ensure our investors that their capital investment is well managed and monitored. As an example, we utilize an affiliated entity, Valerio Consulting, to assist us in this ongoing process. They are a multi-disciplined and energy-centric consulting firm, specializing in marketing, business development, business improvement, engineering, facilities management, and project management.</p>
  </div>
  <div class="page-no">6</div>
  <div class="page-rule"></div>
</section>

<!-- 7: Leadership -->
<section class="page leadership" style="left:14px;top:654px">
  <h2 class="page-title">Leadership</h2>
  <div class="brand"><span class="dot"></span>VALERIO</div>
  <div class="blue-panel">
    <div class="cols body-text" style="font-size:5.2px">
      <div class="col">
        <h4 class="leader-role">Founder + CEO</h4>
        <p>R.J. Valerio is the Founder and Chief Executive Officer of Valerio Capital, LLC. Prior to founding Valerio Capital, R.J. was Chief Executive Officer of Route Nine Collision, Inc., the seventh-largest U.S.-based automotive collision repair company with centers throughout Illinois, Indiana, and Florida.</p>
        <h4 class="leader-role">Senior Managing Director</h4>
        <p>John Carrow IV, CFA is a Senior Managing Director at Valerio Capital Partners, LLC. Prior to joining Valerio Capital Partners, John worked at Lakeshore Trust where he focused on the firm’s capital allocation and requirements. Prior to that, John was a senior analyst at a sub-advised mutual fund company.</p>
        <h4 class="leader-role">Chief Legal Counsel</h4>
        <p>Richard Holm, JD, CPA, is the Chief Legal Officer of Valerio Capital, LLC. Before becoming an attorney, Richard worked for several years as a Certified Public Accountant at a public accounting firm. Following his career in accounting, he practiced law for almost two decades at several prestigious law firms in the Chicagoland area, where he was a partner in the public finance group.</p>
        <h4 class="leader-role">Operating Executive</h4>
        <p>James Corwin is an Operating Executive at Valerio Capital Partners, LLC in charge of manufacturing-related investments. Jim has 30 years of quality leadership experience providing positive results in multiple business units. Most recently, Jim served as the Chief Executive Officer of a coatings and logistics management group providing services to Fortune 50 manufacturing companies.</p>
      </div>
      <div class="col">
        <p>Prior to this, Jim was President and COO of Route Nine Collision, which became one of the largest privately held collision repair operators in the United States.</p>
        <h4 class="leader-role">Operating Executive</h4>
        <p>Anthony Breck, PE is an Operating Executive at Valerio Capital Partners, LLC in charge of energy-related investments. Tony also serves as the president of Valerio Consulting, LLC, an energy-focused management consulting company with clients representing some of the largest original equipment manufacturers that provide products and services in the energy sector.</p>
        <h4 class="leader-role">Senior Associate</h4>
        <p>Dan Ellery is a Senior Associate at Valerio Capital Partners and is responsible for identifying and evaluating investment opportunities, executing investments and supporting portfolio company management teams. Prior to joining Valerio Capital Partners, Dan worked at Whitford &amp; Co. in Chicago, where he focused on mergers and acquisitions for clients in the industrial sector.</p>
        <h4 class="leader-role">Senior Advisor</h4>
        <p>Matthew Marlow is a Senior Advisor at Valerio Capital Partners, LLC in charge of investor client service and business development. Matthew has 25 years experience within the asset management field and has held various positions including Senior Director at a global asset management firm and Founding Partner of a managed futures CTA.</p>
      </div>
    </div>
  </div>
  <div class="page-no">7</div>
  <div class="page-rule"></div>
</section>

<!-- 8: Contact -->
<section class="page contact" style="left:407px;top:654px">
  <h2 class="page-title">Contact Information</h2>
  <div class="brand"><span class="dot"></span>VALERIO</div>
  <div class="photo" role="img" aria-label="Photo of two businessmen reviewing a tablet together"></div>
  <div class="card">
    <div class="avatar" role="img" aria-label="Portrait photo of the senior advisor"></div>
    <div class="name">Matthew D. Marlow</div>
    <div class="role">Senior Advisor</div>
    <div class="address">Valerio Capital Partners<br>410 West Harmon Avenue<br>Suite 1200<br>Chicago, IL 60601</div>
    <div class="reach"><b>Email:</b> mmarlow@valeriocp.example<br><b>Tel:</b> (312) 555-0148<br><b>www.valeriocp.example</b></div>
  </div>
  <div class="page-no">8</div>
  <div class="page-rule"></div>
</section>

</body>
</html>
```